INSURANCE COMPANY POSTCARD

WE ARE A WELL KNOWN INSURANCE AGENCY WORKING UNDER NEW OWNERSHIP USING THE OLD OWNERS NAME STILL, AS OUR TINY COMMUNITY WOULDN'T BE ABLE TO UNDERSTAND THAT WE ARE THE SAME AS BEFORE, JUST A NEW OWNER. WE PROVIDE AUTO, HOME, COMMERCIAL, FLOOD AND EVENT INSURANCE.

Industry/Entity Type

Insurance

```html
<!DOCTYPE html>
<html lang="en">
<head>
<meta charset="utf-8">
<title>Harlow Insurance Agency – Postcard</title>
<link rel="stylesheet" href="https://fonts.googleapis.com/css2?family=Montserrat:wght@600;700&display=swap">
<style>
  :root {
    --brand-navy: #3e4395;
    --crest-lavender: #6b66ad;
    --crest-light: #8e8ac4;
    --paper: #ffffff;
  }
  * { margin: 0; padding: 0; box-sizing: border-box; }
  html, body {
    width: 1200px;
    height: 1200px;
    overflow: hidden;
    background: var(--paper);
  }
  .postcard {
    position: relative;
    width: 1200px;
    height: 1200px;
    background: var(--paper);
    font-family: "Montserrat", Arial, sans-serif;
  }
  .coverage-band {
    position: absolute;
    left: 0;
    top: 134px;
    width: 1200px;
    height: 100px;
    background: var(--brand-navy);
    display: flex;
    justify-content: space-between;
    align-items: center;
    padding: 10px 74px 0 66px;
    list-style: none;
  }
  .coverage-band li {
    color: var(--paper);
    font-weight: 600;
    font-size: 40px;
    letter-spacing: 2px;
    line-height: 1;
  }
  .agency-name {
    position: absolute;
    left: 52px;
    top: 440px;
    width: 612px;
    color: var(--brand-navy);
    font-weight: 700;
    text-align: center;
    line-height: 1;
  }
  .agency-name .primary {
    display: block;
    font-size: 118px;
    letter-spacing: 1px;
  }
  .agency-name .secondary {
    display: block;
    margin-top: 28px;
    font-size: 42px;
  }
  .crest-area {
    position: absolute;
    left: 676px;
    top: 252px;
    width: 464px;
    height: 596px;
    border-radius: 40px 40px 50% 50% / 40px 40px 30% 30%;
    background: radial-gradient(ellipse at 50% 45%, var(--crest-light), var(--crest-lavender) 70%);
  }
  .phone-band {
    position: absolute;
    left: 0;
    top: 866px;
    width: 1200px;
    height: 198px;
    background: var(--brand-navy);
    display: flex;
    align-items: center;
    justify-content: center;
  }
  .phone-number {
    color: var(--paper);
    font-weight: 600;
    font-size: 124px;
    letter-spacing: 6px;
    line-height: 1;
  }
</style>
</head>
<body>
  <main class="postcard">
    <ul class="coverage-band">
      <li>AUTO</li>
      <li>HOME</li>
      <li>LIFE</li>
      <li>HEALTH</li>
      <li>COMMERCIAL</li>
    </ul>

    <h1 class="agency-name">
      <span class="primary">Harlow</span>
      <span class="secondary">Insurance Agency LLC</span>
    </h1>

    <div class="crest-area" role="img" aria-label="Heraldic coat of arms illustration: knight's helmet with crest and mantling above a shield bearing an eagle, with a motto ribbon below"></div>

    <div class="phone-band">
      <p class="phone-number">318-555-0142</p>
    </div>
  </main>
</body>
</html>
```